Business Card Design - Local Discount Club

Looking for a fun business card for a local discount club. One side should be the logo only and the other should be have :

Name
Title
Phone, Email
Website

```html
<!DOCTYPE html>
<html lang="en">
<head>
<meta charset="utf-8">
<title>Harbor Saver Club – Business Card</title>
<link rel="stylesheet" href="https://fonts.googleapis.com/css2?family=Montserrat:wght@400;500;700;800&family=Lato:wght@400;700&display=swap">
<style>
  :root {
    --bg: #e9ebef;
    --card-white: #ffffff;
    --card-navy: #0e1221;
    --brand-blue: #3a5cc2;
    --brand-sky: #3fb2ee;
    --brand-lime: #93e67e;
    --ink: #2a2d35;
    --shadow: 0 14px 34px rgba(14, 18, 33, 0.18);
  }
  * { box-sizing: border-box; margin: 0; padding: 0; }
  html, body {
    width: 1200px;
    height: 800px;
    overflow: hidden;
    background: var(--bg);
  }
  .sheet {
    width: 1200px;
    height: 800px;
    display: flex;
    align-items: center;
    justify-content: center;
    gap: 40px;
  }
  .card {
    width: 540px;
    height: 309px;
    border-radius: 22px;
    box-shadow: var(--shadow);
    position: relative;
    overflow: hidden;
  }

  /* Front: contact side */
  .card--front {
    background: var(--card-white);
    display: flex;
    align-items: center;
    padding: 0 40px 0 44px;
    gap: 34px;
  }
  .brand-name {
    font-family: "Montserrat", sans-serif;
    font-weight: 800;
    color: var(--brand-blue);
    text-transform: uppercase;
    line-height: 1.02;
    letter-spacing: 0.01em;
  }
  .card--front .brand {
    display: flex;
    align-items: center;
    gap: 10px;
    width: 190px;
  }
  .card--front .brand-name { font-size: 30px; }
  .brand-dot {
    width: 14px;
    height: 14px;
    border-radius: 50%;
    background: var(--brand-blue);
    flex: none;
    align-self: flex-start;
    margin-top: 4px;
  }
  .identity { flex: 1; }
  .person-name {
    font-family: "Montserrat", sans-serif;
    font-weight: 800;
    font-size: 25px;
    color: var(--brand-blue);
    text-transform: uppercase;
    letter-spacing: 0.01em;
  }
  .person-title {
    font-family: "Montserrat", sans-serif;
    font-weight: 400;
    font-size: 17px;
    color: var(--brand-sky);
    margin-top: 2px;
  }
  .divider {
    width: 86px;
    height: 4px;
    background: var(--brand-lime);
    margin: 12px 0 14px;
  }
  .contact-list { list-style: none; }
  .contact-item {
    display: flex;
    align-items: center;
    gap: 10px;
    font-family: "Lato", sans-serif;
    font-size: 15px;
    color: var(--ink);
    line-height: 1.75;
  }
  .contact-icon {
    width: 13px;
    height: 13px;
    flex: none;
    fill: var(--brand-sky);
  }

  /* Back: brand side */
  .card--back {
    background: var(--card-navy);
    display: flex;
    align-items: center;
    justify-content: center;
  }
  .card--back .brand {
    display: flex;
    align-items: center;
    gap: 14px;
  }
  .card--back .brand-name {
    font-size: 44px;
    color: var(--brand-sky);
  }
  .card--back .brand-dot {
    width: 20px;
    height: 20px;
    background: var(--brand-sky);
    margin-top: 6px;
  }
</style>
</head>
<body>
  <main class="sheet">
    <section class="card card--front" aria-label="Business card, contact side">
      <div class="brand">
        <span class="brand-name">Harbor<br>Saver<br>Club</span>
        <span class="brand-dot"></span>
      </div>
      <div class="identity">
        <h1 class="person-name">Daniel Brooks</h1>
        <p class="person-title">Founder &amp; CEO</p>
        <div class="divider"></div>
        <ul class="contact-list">
          <li class="contact-item">
            <svg class="contact-icon" viewBox="0 0 24 24" aria-hidden="true"><path d="M6.6 10.8a15.1 15.1 0 0 0 6.6 6.6l2.2-2.2a1 1 0 0 1 1-.25 11.4 11.4 0 0 0 3.6.57 1 1 0 0 1 1 1V20a1 1 0 0 1-1 1A17 17 0 0 1 3 4a1 1 0 0 1 1-1h3.5a1 1 0 0 1 1 1c0 1.25.2 2.45.57 3.57a1 1 0 0 1-.25 1z"/></svg>
            (555) 214-3380
          </li>
          <li class="contact-item">
            <svg class="contact-icon" viewBox="0 0 24 24" aria-hidden="true"><path d="M2 5h20v14H2z M3.5 6.5 12 12.5l8.5-6" stroke="#fff" stroke-width="1.6"/></svg>
            hello@harborsaver.com
          </li>
          <li class="contact-item">
            <svg class="contact-icon" viewBox="0 0 24 24" aria-hidden="true"><circle cx="12" cy="12" r="10"/><path d="M2 12h20M12 2c3 3 3 17 0 20M12 2c-3 3-3 17 0 20" stroke="#fff" stroke-width="1.4" fill="none"/></svg>
            harborsaver.com
          </li>
        </ul>
      </div>
    </section>

    <section class="card card--back" aria-label="Business card, brand side">
      <div class="brand">
        <span class="brand-name">Harbor<br>Saver Club</span>
        <span class="brand-dot"></span>
      </div>
    </section>
  </main>
</body>
</html>
```